Business Card Design

We would like a business card that utilizes our current logo and keeps with the same feel - elegant and organic. Our farm isn't about mass production, it's about excellence, education, beautiful events and flowers - people, culture, and community.

Target Market(s)

Patrons to our farm who are interested in weddings, events, or our flowers and vegetables.

Contact Information for Business Card

Name, address, cell email (Danielle Hoskins, 2716 Wrenfield Rd, Ashbury, CO 80614, cell 30.412.6638, email danielle@wrenfieldacres.com)

```html
<!DOCTYPE html>
<html lang="en">
<head>
<meta charset="utf-8">
<title>Wrenfield Acres – Business Card</title>
<link rel="stylesheet" href="https://fonts.googleapis.com/css2?family=Roboto:wght@300;400;500&display=swap">
<style>
  :root {
    --stage: #e9e6e1;
    --card-white: #ffffff;
    --earth: #a47d55;
    --sage: #7b8f79;
    --sage-light: #b7c4b4;
    --ink-grey: #4a4a4a;
    --on-earth: #ffffff;
  }
  html, body {
    margin: 0;
    padding: 0;
    width: 1200px;
    height: 913px;
    overflow: hidden;
    background: var(--stage);
    font-family: "Roboto", sans-serif;
  }
  .canvas {
    position: relative;
    width: 1200px;
    height: 913px;
  }
  .card {
    position: absolute;
    width: 580px;
    height: 331px;
    border-radius: 18px;
    overflow: hidden;
    box-shadow: 0 10px 28px rgba(0,0,0,0.18);
  }
  .card--front {
    left: 70px;
    top: 110px;
    background: var(--card-white);
  }
  .card--back {
    left: 550px;
    top: 472px;
    background: var(--earth);
  }
  .front-field {
    position: absolute;
    inset: 0;
  }
  .corner-tab {
    position: absolute;
    top: 0;
    right: 36px;
    width: 16px;
    height: 30px;
    background: var(--earth);
  }
  .branch-art {
    position: absolute;
    left: 330px;
    top: 96px;
    width: 200px;
    height: 50px;
    border-radius: 30px 50px 30px 50px;
    background: linear-gradient(100deg, rgba(123,143,121,0.9), rgba(183,196,180,0.8));
  }
  .holder {
    position: absolute;
    right: 62px;
    top: 26px;
    text-align: right;
  }
  .holder-name {
    margin: 0;
    font-weight: 500;
    font-size: 25px;
    line-height: 1.2;
    letter-spacing: 0.5px;
    color: var(--earth);
  }
  .holder-role {
    margin: 2px 0 0;
    font-weight: 400;
    font-size: 14px;
    line-height: 1.2;
    color: var(--ink-grey);
  }
  .brand-mark {
    position: absolute;
    left: 40px;
    top: 112px;
    margin: 0;
    font-weight: 300;
    font-size: 27px;
    color: var(--sage);
  }
  .contact {
    position: absolute;
    right: 28px;
    bottom: 34px;
    margin: 0;
    font-style: normal;
    text-align: right;
    color: var(--on-earth);
    font-size: 15px;
    line-height: 1.45;
  }
  .contact-line {
    display: flex;
    justify-content: flex-end;
    align-items: center;
    gap: 6px;
  }
  .contact-line svg {
    width: 12px;
    height: 12px;
    fill: none;
    stroke: var(--on-earth);
    stroke-width: 1.6;
  }
  .back-brand {
    position: absolute;
    inset: 0;
    display: flex;
    align-items: center;
    justify-content: center;
    margin: 0;
    font-weight: 300;
    font-size: 46px;
    color: var(--on-earth);
  }
</style>
</head>
<body>
<main class="canvas">
  <section class="card card--front" aria-label="Business card front">
    <svg class="front-field" viewBox="0 0 580 331" preserveAspectRatio="none" aria-hidden="true">
      <path d="M150 331 C120 270 150 215 250 175 C340 140 430 122 580 96 L580 331 Z" fill="var(--earth)"/>
      <path d="M150 331 C120 270 150 215 250 175 C340 140 430 122 580 96" fill="none" stroke="var(--sage)" stroke-width="5"/>
    </svg>
    <div class="corner-tab"></div>
    <div class="branch-art" role="img" aria-label="Hand-drawn leafy branch illustration in sage green"></div>
    <div class="holder">
      <h1 class="holder-name">DANIELLE HOSKINS</h1>
      <p class="holder-role">Director</p>
    </div>
    <p class="brand-mark">Wrenfield Acres</p>
    <address class="contact">
      <span class="contact-line">2716 Wrenfield Rd,</span>
      <span class="contact-line">Ashbury, CO 80614</span>
      <span class="contact-line">30.412.6638
        <svg viewBox="0 0 12 12"><path d="M2.5 1.5 L4.5 1.5 L5.2 4 L4 5 C4.6 6.4 5.6 7.4 7 8 L8 6.8 L10.5 7.5 L10.5 9.5 C10.5 10.2 9.8 10.7 9 10.5 C5.4 9.8 2.2 6.6 1.5 3 C1.3 2.2 1.8 1.5 2.5 1.5 Z"/></svg>
      </span>
      <span class="contact-line">danielle@wrenfieldacres.com
        <svg viewBox="0 0 12 12"><rect x="1" y="2.5" width="10" height="7" rx="0.8"/><path d="M1 3 L6 6.8 L11 3"/></svg>
      </span>
    </address>
  </section>

  <section class="card card--back" aria-label="Business card back">
    <p class="back-brand">Wrenfield Acres</p>
  </section>
</main>
</body>
</html>
```